BriarLoom Website Homepage Design

Please provide your idea of homepage for a hosting company. This project is for DESIGN only, no coding.

It must use/combine colors used in logo, clean, modern look.

Homepage must consist of at least 4 sections (example: testimonials, services, and so on. not necesarily all of them). We would like the navigation to be horizontal, but not mandatory.

You can include a preview of services page (optional, not a must).

Number of Pages Required

1 page

Font styles to use
Sans Serif

```html
<!DOCTYPE html>
<html lang="en">
<head>
<meta charset="utf-8">
<title>BriarLoom — Web Hosting Platform</title>
<link href="https://fonts.googleapis.com/css2?family=Libre+Franklin:wght@400;500;600;700&family=IBM+Plex+Sans:wght@400&family=Playfair+Display:wght@900&display=swap" rel="stylesheet">
<style>
:root{
  --blue:#1475d2;
  --blue-dark:#0f5fae;
  --tint:#eaf3fc;
  --paper:#f4f1f1;
  --ink:#111111;
  --text:#3d3d3d;
  --white:#ffffff;
  --footer:#1f1f21;
  --footer-text:#d8d8d8;
}
*{margin:0;padding:0;box-sizing:border-box}
html,body{width:1200px;height:3453px;overflow:hidden}
body{font-family:"Libre Franklin",Arial,sans-serif;color:var(--text);background:var(--white);position:relative}
.serif{font-family:"Playfair Display",Georgia,serif;font-weight:900;color:var(--ink)}
section,header,footer,.topbar{position:relative;width:1200px}
.abs{position:absolute}

/* top bar */
.topbar{height:31px;background:var(--blue);color:var(--white);font-size:12px}
.topbar .follow{left:132px;top:9px;display:flex;align-items:center;gap:10px}
.topbar .dot{width:7px;height:7px;border-radius:50%;background:var(--white);display:inline-block}
.topbar .follow .sep{width:1px;height:14px;background:rgba(255,255,255,.5);margin:0 2px}
.topbar .contact{right:132px;top:8px;display:flex;gap:30px;font-size:13px}
.topbar .contact span{display:flex;align-items:center;gap:7px}

/* header */
header{height:82px;background:var(--white)}
.brand{font-family:"Libre Franklin",Arial,sans-serif;font-weight:700;color:var(--blue);font-size:38px;letter-spacing:1px;display:flex;align-items:center;gap:10px}
header .brand{left:132px;top:20px}
.brand .mark{width:16px;height:16px;background:var(--blue);border-radius:3px}
.nav{right:132px;top:32px;display:flex;gap:47px;font-size:15px;font-weight:600;color:var(--ink)}
.nav a{color:inherit;text-decoration:none;position:relative}
.nav a.active{color:var(--blue)}
.nav a.active::after{content:"";position:absolute;left:0;right:0;bottom:-7px;height:2px;background:var(--blue)}

/* hero */
.hero{height:619px;background:radial-gradient(ellipse at 50% 55%,#2a3aa0 0%,#141c54 45%,#070a1e 100%);text-align:center;color:var(--white)}
.hero h1{font-family:"Playfair Display",Georgia,serif;font-weight:900;font-size:50px;position:absolute;top:195px;left:0;right:0}
.hero p{font-family:"IBM Plex Sans",Arial,sans-serif;font-size:20px;position:absolute;top:274px;left:0;right:0}
.hero .btn{position:absolute;left:524px;top:347px;width:152px;height:52px;background:var(--blue);font-size:17px;font-weight:500;line-height:52px;color:var(--white)}
.hero .dots{position:absolute;top:568px;left:0;right:0;display:flex;justify-content:center;gap:10px}
.hero .dots i{width:7px;height:7px;border-radius:50%;background:var(--white)}
.hero .dots i.on{background:var(--blue)}

.section-title{position:absolute;left:0;right:0;text-align:center;font-size:29px}
.section-title::after{content:"";display:block;width:56px;height:2px;background:var(--blue);margin:17px auto 0}

/* services */
.services{height:703px;background:var(--paper)}
.services .section-title{top:45px}
.card{position:absolute;width:453px;height:232px;background:var(--white);overflow:hidden;box-shadow:0 1px 4px rgba(0,0,0,.04)}
.card .halo{position:absolute;left:-28px;top:-38px;width:178px;height:178px;border-radius:50%;background:var(--tint)}
.card svg{position:absolute;left:30px;top:35px}
.card h3{position:absolute;left:183px;top:26px;font-size:21px}
.card p{position:absolute;left:183px;top:66px;width:240px;font-size:12.5px;line-height:17.5px;color:var(--text)}
.card .mini{position:absolute;left:186px;top:172px;width:80px;height:27px;background:var(--blue);color:var(--white);font-size:10px;font-weight:700;line-height:27px;text-align:center}

/* welcome */
.welcome{height:568px;background:var(--blue);color:var(--white)}
.welcome h2{position:absolute;left:130px;top:165px;font-family:"Playfair Display",Georgia,serif;font-weight:900;font-size:36px;color:var(--white)}
.welcome .lead{position:absolute;left:133px;top:232px;width:430px;font-size:17px;line-height:24px;font-weight:500}
.welcome .body{position:absolute;left:133px;top:338px;width:440px;font-size:13.7px;line-height:20px}
.welcome .outline{position:absolute;left:132px;top:474px;width:102px;height:34px;border:2px solid var(--white);font-size:11.5px;font-weight:700;line-height:30px;text-align:center}
.feature{position:absolute;left:650px;width:415px;height:162px}
.feature svg{position:absolute;left:28px;top:38px}
.feature h4{position:absolute;left:119px;top:32px;font-family:"Playfair Display",Georgia,serif;font-weight:900;font-size:21px;color:var(--white)}
.feature p{position:absolute;left:119px;top:70px;width:300px;font-family:"IBM Plex Sans",Arial,sans-serif;font-size:14px;line-height:20px}
.feature + .feature{border-top:1px solid rgba(255,255,255,.25)}

/* why */
.why{height:560px;background:var(--white)}
.why .section-title{top:52px}
.point{position:absolute;width:300px}
.point .icon{position:absolute;left:0;top:0;width:75px;height:75px;border-radius:50%;background:var(--blue);display:flex;align-items:center;justify-content:center}
.point h5{position:absolute;left:95px;top:-15px;width:190px;font-size:14.5px;font-weight:500;color:var(--ink);line-height:20px}
.point p{position:absolute;left:95px;top:32px;width:185px;font-size:12.5px;line-height:16px;color:var(--text)}

/* testimonials */
.testimonials{height:544px;background:var(--paper)}
.testimonials .section-title{top:44px}
.quote{position:absolute;top:145px;width:296px;height:344px;background:var(--white)}
.quote .mark{position:absolute;left:38px;top:30px;font-family:"Playfair Display",Georgia,serif;font-weight:900;font-size:26px;color:var(--text)}
.quote p{position:absolute;left:38px;top:72px;width:225px;font-size:14.5px;line-height:21px;color:var(--text)}
.quote .who{position:absolute;left:38px;top:286px;font-family:"Playfair Display",Georgia,serif;font-weight:900;font-size:14px;color:var(--blue)}
.quote .who::before{content:"";display:block;width:42px;height:2px;background:var(--blue);margin-bottom:11px}
.arrow{position:absolute;top:303px}

/* footer */
footer{height:346px;background:var(--footer);color:var(--footer-text);font-size:12px}
footer .brand{position:absolute;left:132px;top:95px}
footer h6{font-size:13px;font-weight:700;color:var(--white);letter-spacing:.5px;margin-bottom:21px}
.fcol{position:absolute;top:52px}
.fcol ul{list-style:none}
.fcol.menu li{line-height:20px;color:var(--white)}
.fitem{display:flex;gap:11px;align-items:flex-start;margin-bottom:22px;line-height:15px;color:var(--white)}
.fitem .c{width:22px;height:22px;border-radius:50%;background:var(--white);flex:none;margin-top:3px;display:flex;align-items:center;justify-content:center}
footer .copy{position:absolute;left:0;right:0;top:314px;text-align:center;font-size:9px;color:var(--footer-text)}
</style>
</head>
<body>

<div class="topbar">
  <div class="abs follow">Follow us <span class="sep"></span><i class="dot"></i><i class="dot"></i><i class="dot"></i></div>
  <div class="abs contact">
    <span><svg width="11" height="9" viewBox="0 0 11 9"><rect width="11" height="9" rx="1" fill="#fff"/><path d="M0 1l5.5 4L11 1" stroke="#1475d2" fill="none"/></svg>info@briarloom.com</span>
    <span><svg width="11" height="11" viewBox="0 0 24 24"><path fill="#fff" d="M6.6 10.8a15 15 0 006.6 6.6l2.2-2.2c.3-.3.7-.4 1-.2 1.1.4 2.3.6 3.6.6.6 0 1 .4 1 1V20c0 .6-.4 1-1 1A17 17 0 013 4c0-.6.4-1 1-1h3.5c.6 0 1 .4 1 1 0 1.3.2 2.5.6 3.6.1.3 0 .7-.2 1z"/></svg>(555).014.2270</span>
    <span><svg width="11" height="10" viewBox="0 0 11 10"><ellipse cx="5.5" cy="4" rx="5.5" ry="4" fill="#fff"/><path d="M2 7l-1 3 4-2z" fill="#fff"/></svg>Support</span>
  </div>
</div>

<header>
  <div class="abs brand"><span>BRIARLOOM</span><span class="mark"></span></div>
  <nav class="abs nav">
    <a class="active">HOME</a><a>ABOUT US</a><a>SERVICES</a><a>PLANS</a><a>CONTACT US</a>
  </nav>
</header>

<section class="hero" role="img" aria-label="Photograph of a data center aisle lined with server racks glowing blue">
  <h1>Web Hosting Platform</h1>
  <p>Lorem Ipsum is simply dummy text of the printing</p>
  <div class="btn">READ MORE</div>
  <div class="dots"><i></i><i></i><i class="on"></i><i></i><i></i></div>
</section>

<section class="services">
  <h2 class="section-title serif">Our Services</h2>

  <div class="card" style="left:132px;top:148px">
    <div class="halo"></div>
    <svg width="80" height="80" viewBox="0 0 80 80" fill="none" stroke="#1475d2" stroke-width="2.5">
      <circle cx="40" cy="40" r="37"/><ellipse cx="40" cy="40" rx="16" ry="37"/><path d="M6 25h68M6 55h68M40 3v74"/>
      <rect x="1" y="30" width="78" height="20" rx="4" fill="#eaf3fc"/>
      <text x="40" y="46" font-family="Libre Franklin,Arial,sans-serif" font-size="15" fill="#1475d2" stroke="none" text-anchor="middle" font-weight="600">WWW</text>
    </svg>
    <h3 class="serif">Domains</h3>
    <p>Sed ut perspiciatis unde omnis iste natus error sit voluptatem accus antium doloremque laudantium totam rem aperiam eaque ipsa quae ab illo inve ntore veritatis et quasi architecto.</p>
    <div class="mini">READ MORE</div>
  </div>

  <div class="card" style="left:614px;top:148px">
    <div class="halo"></div>
    <svg width="80" height="62" viewBox="0 0 80 62" fill="none" stroke="#1475d2" stroke-width="2.5">
      <rect x="2" y="2" width="76" height="58" rx="3"/><path d="M2 12h76"/><rect x="9" y="20" width="28" height="13"/><rect x="43" y="20" width="28" height="13"/><path d="M9 40h62M9 47h30M45 47h26M9 53h62"/>
    </svg>
    <h3 class="serif">Websites</h3>
    <p>Sed ut perspiciatis unde omnis iste natus error sit voluptatem accus antium doloremque laudantium totam rem aperiam eaque ipsa quae ab illo inve ntore veritatis et quasi architecto.</p>
    <div class="mini">READ MORE</div>
  </div>

  <div class="card" style="left:132px;top:408px">
    <div class="halo"></div>
    <svg width="70" height="78" viewBox="0 0 70 78" fill="none" stroke="#1475d2" stroke-width="2.5">
      <rect x="6" y="2" width="58" height="14" rx="3"/><rect x="6" y="21" width="58" height="14" rx="3"/><rect x="6" y="40" width="58" height="14" rx="3"/><path d="M35 54v12M1 74h68"/><rect x="29" y="64" width="12" height="8"/>
    </svg>
    <h3 class="serif">Hosting</h3>
    <p>Sed ut perspiciatis unde omnis iste natus error sit voluptatem accus antium doloremque laudantium totam rem aperiam eaque ipsa quae ab illo inve ntore veritatis et quasi architecto.</p>
    <div class="mini">READ MORE</div>
  </div>

  <div class="card" style="left:614px;top:408px">
    <div class="halo"></div>
    <svg width="66" height="66" viewBox="0 0 66 66" fill="none" stroke="#1475d2" stroke-width="2.5">
      <rect x="12" y="4" width="42" height="34" fill="#cfe3f7"/><path d="M2 26v38h62V26L33 48z"/><path d="M2 64l24-20M64 64L40 44"/>
    </svg>
    <h3 class="serif">Email</h3>
    <p>Sed ut perspiciatis unde omnis iste natus error sit voluptatem accus antium doloremque laudantium totam rem aperiam eaque ipsa quae ab illo inve ntore veritatis et quasi architecto.</p>
    <div class="mini">READ MORE</div>
  </div>
</section>

<section class="welcome">
  <svg class="abs" style="left:132px;top:65px" width="82" height="68" viewBox="0 0 82 68">
    <g fill="#fff"><rect width="82" height="20" rx="4"/><rect y="24" width="82" height="20" rx="4"/><rect y="48" width="82" height="20" rx="4"/></g>
    <g fill="#1475d2"><rect x="8" y="5" width="2" height="10"/><rect x="12" y="5" width="2" height="10"/><rect x="16" y="5" width="2" height="10"/><circle cx="72" cy="10" r="3"/>
    <rect x="8" y="29" width="2" height="10"/><rect x="12" y="29" width="2" height="10"/><rect x="16" y="29" width="2" height="10"/><circle cx="72" cy="34" r="3"/>
    <rect x="8" y="53" width="2" height="10"/><rect x="12" y="53" width="2" height="10"/><rect x="16" y="53" width="2" height="10"/><circle cx="72" cy="58" r="3"/></g>
  </svg>
  <h2>Welcome to BriarLoom</h2>
  <p class="lead">Sed ut perspiciatis unde omnis iste natus error sit volup tatem accusantium doloremque laudantium, totam rem aperiam, eaque ipsa quae ab illo.</p>
  <p class="body">But I must explain to you how all this mistaken idea of denouncing pleasure and praising pain was born and I will give you a complete account of the system, and expound the actual teachings of the great explorer of the truth, the master-builder of human happi ness. No one rejects, dislikes, or avoids pleasure itself.</p>
  <div class="outline">READ MORE</div>

  <div class="feature" style="top:0">
    <svg width="64" height="66" viewBox="0 0 64 66" fill="none" stroke="#fff" stroke-width="2.5"><path d="M8 34v-6a24 24 0 0148 0v6"/><rect x="2" y="32" width="10" height="20" rx="4"/><rect x="52" y="32" width="10" height="20" rx="4"/><path d="M57 52v4a6 6 0 01-6 6H38"/><rect x="28" y="58" width="10" height="7" rx="3"/></svg>
    <h4>24/7 Friendly Support</h4>
    <p>I will give you a complete account of the system, and expound the actual teachings of the great explorer of the truth.</p>
  </div>
  <div class="feature" style="top:162px">
    <svg width="54" height="58" viewBox="0 0 54 58" fill="none" stroke="#fff" stroke-width="2.5"><path d="M3 0v56h51"/><path d="M48 10L20 38M20 22v16h16"/><path d="M3 14h5M3 26h5M3 38h5"/></svg>
    <h4>Low Cost</h4>
    <p>I will give you a complete account of the system, and expound the actual teachings of the great explorer of the truth.</p>
  </div>
  <div class="feature" style="top:324px">
    <svg width="54" height="52" viewBox="0 0 54 52" fill="none" stroke="#fff" stroke-width="2.5"><rect x="2" y="2" width="50" height="48" rx="4"/><path d="M2 12h50M12 22h28l-6-6M42 36H14l6 6"/></svg>
    <h4>Free Website Transfer</h4>
    <p>I will give you a complete account of the system, and expound the actual teachings of the great explorer of the truth.</p>
  </div>
</section>

<section class="why">
  <h2 class="section-title serif">Why choose BriarLoom</h2>

  <div class="point" style="left:132px;top:182px">
    <div class="icon"><svg width="34" height="40" viewBox="0 0 34 40" fill="#fff"><rect width="34" height="8" rx="2"/><rect y="11" width="34" height="8" rx="2"/><rect y="22" width="34" height="8" rx="2"/><rect x="16" y="30" width="2" height="6"/><rect y="36" width="34" height="2"/></svg></div>
    <h5>RELIABLE SERVERS AND TECHNOLOGY</h5>
    <p>Sed ut perspiciatis unde omnis iste natus error sit voluptatem accus antium doloremque laudantium totam rem ap eriam eaque ipsa</p>
  </div>
  <div class="point" style="left:461px;top:182px">
    <div class="icon"><svg width="40" height="40" viewBox="0 0 40 40" fill="none" stroke="#fff" stroke-width="3"><circle cx="20" cy="20" r="17"/><path d="M20 20l8-8M9 24h4M27 24h4M20 8v3"/></svg></div>
    <h5>OPTIMIZED FOR SPEED &amp; PERFORMANCE</h5>
    <p>Sed ut perspiciatis unde omnis iste natus error sit voluptatem accus antium doloremque laudantium totam rem ap eriam eaque ipsa</p>
  </div>
  <div class="point" style="left:798px;top:182px">
    <div class="icon"><svg width="34" height="40" viewBox="0 0 34 40" fill="none" stroke="#fff" stroke-width="3"><path d="M17 2l14 5v12c0 9-6 16-14 19C9 35 3 28 3 19V7z"/><path d="M11 20l5 5 8-9"/></svg></div>
    <h5>COMMITMENT TO SECURITY</h5>
    <p>Sed ut perspiciatis unde omnis iste natus error sit voluptatem accus antium doloremque laudantium totam rem ap eriam eaque ipsa</p>
  </div>

  <div class="point" style="left:132px;top:364px">
    <div class="icon"><svg width="40" height="40" viewBox="0 0 40 40"><circle cx="20" cy="20" r="13" fill="none" stroke="#fff" stroke-width="7" stroke-dasharray="6 4.2"/><circle cx="20" cy="20" r="11" fill="#fff"/><circle cx="20" cy="20" r="5" fill="#1475d2"/></svg></div>
    <h5>INDEPENDENTLY OWNED AND OPERATED</h5>
    <p>Sed ut perspiciatis unde omnis iste natus error sit voluptatem accus antium doloremque laudantium totam rem ap eriam eaque ipsa</p>
  </div>
  <div class="point" style="left:461px;top:364px">
    <div class="icon"><svg width="44" height="44" viewBox="0 0 44 44" fill="none" stroke="#fff" stroke-width="2.5"><path d="M8 34A18 18 0 018 10M36 34a18 18 0 000-24"/><circle cx="22" cy="22" r="11"/><path fill="#fff" stroke="none" d="M22 15l2 4.5 5 .5-3.8 3.3 1.1 4.9L22 25.7l-4.3 2.5 1.1-4.9L15 20l5-.5z"/></svg></div>
    <h5>AWARD-WINNING SUPPORT</h5>
    <p>Sed ut perspiciatis unde omnis iste natus error sit voluptatem accus antium doloremque laudantium totam rem ap eriam eaque ipsa</p>
  </div>
  <div class="point" style="left:798px;top:364px">
    <div class="icon"><svg width="38" height="38" viewBox="0 0 38 38" fill="#fff"><rect x="1" y="16" width="8" height="20" rx="1"/><path d="M12 17l7-14c3 0 5 2 4 6l-2 6h12c2 0 4 2 3 5l-3 12c-1 2-2 3-4 3H12z"/></svg></div>
    <h5>100% SATISFACTION GUARANTEED</h5>
    <p>Sed ut perspiciatis unde omnis iste natus error sit voluptatem accus antium doloremque laudantium totam rem ap eriam eaque ipsa</p>
  </div>
</section>

<section class="testimonials">
  <h2 class="section-title serif">Testimonials</h2>
  <svg class="arrow" style="left:70px" width="14" height="24" viewBox="0 0 14 24" fill="none" stroke="#777" stroke-width="2"><path d="M12 2L2 12l10 10"/></svg>
  <svg class="arrow" style="left:1112px" width="14" height="24" viewBox="0 0 14 24" fill="none" stroke="#777" stroke-width="2"><path d="M2 2l10 10-10 10"/></svg>

  <div class="quote" style="left:132px"><span class="mark">“</span><p>But I must explain to you how all this mistaken idea of denouncing pleasure and praising pain was born and I will give you a comp lete account of the system, and expound the actual teachings of the great explorer of the truth, the master-builder of human happiness.</p><span class="who">Daniel</span></div>
  <div class="quote" style="left:452px"><span class="mark">“</span><p>But I must explain to you how all this mistaken idea of denouncing pleasure and praising pain was born and I will give you a comp lete account of the system, and expound the actual teachings of the great explorer of the truth, the master-builder of human happiness.</p><span class="who">Daniel</span></div>
  <div class="quote" style="left:771px"><span class="mark">“</span><p>But I must explain to you how all this mistaken idea of denouncing pleasure and praising pain was born and I will give you a comp lete account of the system, and expound the actual teachings of the great explorer of the truth, the master-builder of human happiness.</p><span class="who">Daniel</span></div>
</section>

<footer>
  <div class="brand"><span>BRIARLOOM</span><span class="mark"></span></div>
  <div class="fcol menu" style="left:467px">
    <h6>MENU</h6>
    <ul><li>HOME</li><li>ABOUT US</li><li>SERVICES</li><li>PLANS</li><li>CONTACT US</li></ul>
  </div>
  <div class="fcol" style="left:666px">
    <h6>CONTACT US</h6>
    <div class="fitem"><span class="c"><svg width="8" height="11" viewBox="0 0 8 11"><path fill="#1f1f21" d="M4 0a4 4 0 014 4c0 3-4 7-4 7S0 7 0 4a4 4 0 014-4z"/><circle cx="4" cy="4" r="1.4" fill="#fff"/></svg></span><span>2217 Larkspur Lane<br>Fairvale, CA 90410</span></div>
    <div class="fitem"><span class="c"><svg width="10" height="10" viewBox="0 0 24 24"><path fill="#1f1f21" d="M6.6 10.8a15 15 0 006.6 6.6l2.2-2.2c.3-.3.7-.4 1-.2 1.1.4 2.3.6 3.6.6.6 0 1 .4 1 1V20c0 .6-.4 1-1 1A17 17 0 013 4c0-.6.4-1 1-1h3.5c.6 0 1 .4 1 1 0 1.3.2 2.5.6 3.6.1.3 0 .7-.2 1z"/></svg></span><span>Call Us<br>555.014.2270</span></div>
    <div class="fitem"><span class="c"><svg width="10" height="8" viewBox="0 0 11 9"><rect width="11" height="9" rx="1" fill="#1f1f21"/><path d="M0 1l5.5 4L11 1" stroke="#fff" fill="none"/></svg></span><span>E mail Us<br>info@briarloom.com</span></div>
  </div>
  <div class="fcol" style="left:960px">
    <h6>FOLLOW US</h6>
    <div class="fitem"><span class="c"></span><span>Like us on<br>LINKORY</span></div>
    <div class="fitem"><span class="c"></span><span>Follow us on<br>CHIRPLINE</span></div>
    <div class="fitem"><span class="c"></span><span>Follow us on<br>WORKFOLK</span></div>
  </div>
  <p class="copy">Copyright © 2021 All Rights Reserved</p>
</footer>

</body>
</html>
```